The Harbourlight Dental centre, the Zentrix of dentistry

New concept of running a dental practice by having a walk in practice
WE ARE A HUSBAND AND WIFE TEAM

Really modern and sophisticated, we want it to feel different from the traditional dental practice.
we want it split into different pages:CONTACT US
LOCATION: Information about our location since patients often confuse us with the practice across the road
ABOUT US:
Opening hours - & 7 Days, We offer a weekend service
WALK IN: We offer a walk in service for dental treatments
TREATMENTS we offer

DENTAL ADVICE: Free dentist advise call back- So a dentist will call you back for free to discuss

Target Market(s)

Everyone

Industry/Entity Type

Dental

Coding

Coded - Design and coding required

Number of Pages Required

5+ page

Requirements
Must have
• First page
• * changing pictures
• *opening times
• * our walk in concept I.e. no appointment needed
• *logo
• * links in to carely hub (online booking system in Australia)
• * address /phone number/email
• * possible videos
• Second page
• meet the team
• third page
• dental treatments/walk in treatments
• fourth page
• dental advice with vid nest videos
• Fifth page
• contact us/maps/ we get confused with the dental practice across the road
• We would also like a giving back page. In this please include the photo's below of our dental mission in Guatemala, where by we did treatment for patients as part of a charity.
Nice to have
• Changing pictures on the home screen
• videos linked to home page

```html
<!DOCTYPE html>
<html lang="en">
<head>
<meta charset="utf-8">
<title>The Harbourlight Dental centre</title>
<link href="https://fonts.googleapis.com/css2?family=Roboto:wght@300;400;500;700&display=swap" rel="stylesheet">
<style>
:root{
  --blue:#1ba3e0;
  --blue-dark:#0f7fb3;
  --green:#9ccb3b;
  --ink:#2b2b2b;
  --muted:#6f6f6f;
  --line:#d7d7d7;
  --panel:#f4f3f4;
  --footer:#2d2e3b;
  --footer-line:#555766;
  --white:#ffffff;
}
*{margin:0;padding:0;box-sizing:border-box}
html,body{width:1200px;height:2490px;overflow:hidden}
body{position:relative;background:var(--white);font-family:'Roboto',Arial,sans-serif;color:var(--ink)}
.abs{position:absolute}

/* header */
.brand{left:155px;top:18px;display:flex;align-items:center;gap:10px}
.brand-mark{width:34px;height:34px;border-radius:50%;background:var(--green)}
.brand-name{font-size:19px;font-weight:700;color:var(--green);line-height:1.05;width:240px}
.hours{left:805px;top:24px;display:flex;gap:12px;align-items:center}
.hours-label{font-size:13px;color:var(--muted)}
.hours-value{font-size:15px;color:var(--blue)}

/* nav */
.nav{left:0;top:88px;width:1200px;height:40px;background:var(--blue)}
.nav-links{left:155px;top:88px;height:40px;display:flex;list-style:none}
.nav-links li{font-size:13px;font-weight:500;color:var(--white);padding:0 12px;line-height:40px}
.nav-links li.active{background:var(--green);padding:0 14px}
.call{left:810px;top:88px;width:390px;height:40px;background:var(--green);clip-path:polygon(12px 0,100% 0,100% 100%,0 100%);display:flex;align-items:center;gap:8px;padding-left:20px;color:var(--white);font-size:20px;font-weight:500}

/* hero */
.hero{left:0;top:128px;width:1200px;height:400px;background:linear-gradient(100deg,#6f7a86 0%,#8d9098 40%,#a6847e 70%,#5a4b48 100%)}
.hero-title{left:0;top:220px;width:1200px;text-align:center;font-size:48px;font-weight:500;color:var(--white)}
.hero-text{left:330px;top:276px;width:540px;text-align:center;font-size:23px;font-weight:300;color:var(--white);line-height:1.4}
.btn{display:inline-block;text-align:center;font-size:12px;font-weight:500;letter-spacing:.5px;border-radius:16px}
.btn-solid{background:var(--blue);color:var(--white)}
.btn-outline{border:1px solid var(--blue);color:var(--blue);background:var(--white)}
.hero-btn{left:535px;top:362px;width:128px;height:30px;line-height:30px}
.arrow-left{left:0;top:310px;width:42px;height:40px;background:#4a4f56}
.arrow-right{left:1155px;top:308px;width:45px;height:44px;background:var(--blue)}

/* booking */
.book-title{left:155px;top:640px;font-size:29px;font-weight:500;line-height:1.3;width:520px}
.book-sub{left:155px;top:716px;font-size:19px;font-weight:300;color:#444}
.book-note{left:155px;top:760px;width:530px;font-size:13px;line-height:1.45;color:#444}
.book-btn-a{left:155px;top:849px;width:158px;height:32px;line-height:32px}
.book-btn-b{left:337px;top:849px;width:95px;height:32px;line-height:30px}
.phone-art{left:770px;top:575px;width:260px;height:375px;border-radius:30px;background:linear-gradient(160deg,#e9ecef,#c3c7cc)}

/* services */
.services{left:0;top:972px;width:1200px;height:396px;background:var(--panel)}
.section-title{font-size:23px;font-weight:400;color:#333}
.section-title em{font-style:normal;color:var(--blue);font-weight:500}
.rule{height:1px;background:var(--line)}
.svc-col{top:1095px;width:300px;text-align:center}
.svc-icon{margin:25px auto 0;width:72px;height:72px;border-radius:50%;border:1.5px solid #555;display:flex;align-items:center;justify-content:center;background:var(--white)}
.svc-name{margin-top:22px;font-size:19px;color:#333}
.svc-text{margin:10px auto 0;width:225px;font-size:12.5px;line-height:1.3;color:#555}
.divider{top:1095px;width:1px;height:220px;background:var(--line)}
.circle-arrow{width:24px;height:24px;border-radius:50%;border:1px solid #999;display:flex;align-items:center;justify-content:center}
.circle-arrow.on{border-color:var(--blue)}

/* video & quotes */
.video{left:155px;top:1476px;width:433px;height:290px;background:linear-gradient(120deg,#7c6a5c,#c9a993 55%,#e3d0c2)}
.play{left:350px;top:1578px;width:46px;height:46px;border-radius:50%;background:rgba(40,40,40,.75);border:2px solid #ddd}
.video-caption{left:235px;top:1645px;width:273px;text-align:center;font-size:19px;font-weight:500;color:var(--white);line-height:1.25}
.quote-mark{font-size:80px;font-weight:700;color:#c9c9c9;line-height:1;font-family:Georgia,serif}
.quote-text{left:635px;top:1535px;width:410px;font-size:12.5px;line-height:1.55;color:#555}
.avatar{left:635px;top:1693px;width:72px;height:72px;border-radius:50%;background:linear-gradient(#d9d9d9,#9b9b9b)}
.author{left:730px;top:1710px;font-size:15px;color:#333}
.author small{display:block;font-size:12px;color:#777;margin-top:3px}

/* team */
.view-team{left:973px;top:1828px;font-size:14px;font-style:italic;color:#333;text-decoration:underline}
.card{top:1880px;width:205px;height:222px}
.card-photo{width:205px;height:185px;background:linear-gradient(#e8edf1,#c8cfd5)}
.card-bar{position:relative;height:37px;background:var(--blue);color:var(--white);padding:6px 0 0 16px}
.card-bar b{display:block;font-size:12px;font-weight:500}
.card-bar span{display:block;font-size:10px}
.card-tag{position:absolute;right:0;top:0;width:80px;height:37px;background:var(--blue-dark);clip-path:polygon(14px 0,100% 0,100% 100%,0 100%);display:flex;gap:6px;align-items:center;justify-content:center}
.card-tag i{width:8px;height:8px;border-radius:50%;background:#bfe6f7}

/* footer */
.footer{left:0;top:2150px;width:1200px;height:275px;background:var(--footer)}
.foot-title{font-size:14px;color:var(--white);letter-spacing:.3px}
.foot-rule{height:1px;background:var(--footer-line)}
.foot-text{font-size:12px;color:#b9bac3;line-height:1.4}
.field{left:155px;width:205px;height:25px;border:1px solid var(--footer-line);font-size:11px;color:#8a8c98;padding:5px 8px}
.submit{left:155px;top:2355px;width:80px;height:27px;line-height:27px;border-radius:14px;background:var(--blue);color:var(--white);font-size:12px;font-weight:500;text-align:center}
.quick{left:535px;top:2240px;list-style:none}
.quick li{font-size:12px;color:#b9bac3;line-height:20px}
.quick li::before{content:"•";margin-right:12px}
.quick li.active{color:var(--blue)}
.copyright{left:155px;top:2452px;font-size:12px;color:#444}
.social{top:2448px;width:24px;height:24px;border-radius:50%;background:#1d62a8}
</style>
</head>
<body>

<header>
  <div class="abs brand"><span class="brand-mark"></span><span class="brand-name">The Harbourlight Dental centre</span></div>
  <div class="abs hours">
    <svg width="26" height="26" viewBox="0 0 26 26"><circle cx="13" cy="13" r="11" fill="none" stroke="#444" stroke-width="1.6"/><path d="M13 6v7h5" fill="none" stroke="#444" stroke-width="1.6"/></svg>
    <div><div class="hours-label">Opening Hours:</div><div class="hours-value">8 AM TO 8PM 7 Days A Week</div></div>
  </div>
</header>

<nav>
  <div class="abs nav"></div>
  <ul class="abs nav-links">
    <li class="active">Home</li><li>About Us</li><li>Team</li><li>Dental Treatments</li><li>Dental Advice</li><li>Contact Us</li>
  </ul>
  <div class="abs call">Call Us
    <svg width="24" height="24" viewBox="0 0 24 24"><circle cx="12" cy="12" r="10.5" fill="none" stroke="#fff" stroke-width="1.6"/><path d="M8.5 7c-1 1 -1 3 1.5 6s5 3.5 6 2.5l-1.8-1.8-1.3 .8c-1-.5-2.5-2-3-3l.8-1.3z" fill="#fff"/></svg>
    08 5550 1847</div>
</nav>

<section>
  <div class="abs hero" role="img" aria-label="Photo of a dentist examining a smiling patient's teeth"></div>
  <h1 class="abs hero-title">Nervous, Don’t Worry</h1>
  <p class="abs hero-text">we can help relieve your fears, come in and have a chat with our friendly dentists.</p>
  <span class="abs btn btn-solid hero-btn">CONNECT NOW</span>
  <div class="abs arrow-left"><svg width="42" height="40" viewBox="0 0 42 40"><path d="M25 20H15m4-5-5 5 5 5" fill="none" stroke="#fff" stroke-width="2.5"/></svg></div>
  <div class="abs arrow-right"><svg width="45" height="44" viewBox="0 0 45 44"><path d="M17 22h11m-4-5 5 5-5 5" fill="none" stroke="#fff" stroke-width="2.5"/></svg></div>
</section>

<section>
  <h2 class="abs book-title">Find and book health appointments, 24/7 with.</h2>
  <p class="abs book-sub">Walk in appointments available, call today to find out more!</p>
  <p class="abs book-note">We Understand That Everyone Has A Busy Life And We Want Dental Treatment To Be Accessible For All.</p>
  <span class="abs btn btn-solid book-btn-a">APPOINTMENT NOW</span>
  <span class="abs btn btn-outline book-btn-b">CALL US</span>
  <div class="abs phone-art" role="img" aria-label="Illustration of a smartphone showing a chat about booking a doctor's appointment"></div>
</section>

<section>
  <div class="abs services"></div>
  <h2 class="abs section-title" style="left:155px;top:1015px">Our <em>Services</em></h2>
  <div class="abs rule" style="left:133px;top:1055px;width:935px"></div>
  <div class="abs circle-arrow" style="left:986px;top:1017px"><svg width="10" height="10"><path d="M7 1 3 5l4 4" fill="none" stroke="#777" stroke-width="1.5"/></svg></div>
  <div class="abs circle-arrow on" style="left:1020px;top:1017px"><svg width="10" height="10"><path d="M3 1l4 4-4 4" fill="none" stroke="#1ba3e0" stroke-width="1.5"/></svg></div>

  <div class="abs svc-col" style="left:147px">
    <div class="svc-icon"><svg width="36" height="40" viewBox="0 0 36 40"><path d="M8 4c4-2 7 1 10 1s6-3 10-1 5 8 3 14-3 18-6 18-3-10-7-10-4 10-7 10-4-12-6-18S4 6 8 4z" fill="none" stroke="#444" stroke-width="1.6"/></svg></div>
    <div class="svc-name">Extractions</div>
    <p class="svc-text">We will always try to save a healthy tooth. However sometimes it does become necessary to take...</p>
  </div>
  <div class="abs divider" style="left:448px"></div>
  <div class="abs svc-col" style="left:451px">
    <div class="svc-icon"><svg width="40" height="40" viewBox="0 0 40 40"><path d="M10 8c4-2 7 1 10 1s6-3 10-1 5 8 3 14-3 16-6 16-3-9-7-9-4 9-7 9-4-10-6-16S6 10 10 8z" fill="none" stroke="#444" stroke-width="1.6"/><path d="M10 14h20" stroke="#444" stroke-width="3"/></svg></div>
    <div class="svc-name">Dentures</div>
    <p class="svc-text">Dentures are used to replace lost or missing teeth. People wear dentures so they can enjoy a healthy...</p>
  </div>
  <div class="abs divider" style="left:752px"></div>
  <div class="abs svc-col" style="left:760px">
    <div class="svc-icon"><svg width="36" height="40" viewBox="0 0 36 40"><path d="M8 4c4-2 7 1 10 1s6-3 10-1 5 8 3 14-3 18-6 18-3-10-7-10-4 10-7 10-4-12-6-18S4 6 8 4z" fill="none" stroke="#444" stroke-width="1.6"/><path d="M18 10v14" stroke="#444" stroke-width="2"/></svg></div>
    <div class="svc-name">Root Canal Treatment</div>
    <p class="svc-text">Root canal therapy (RCT) is a technique used to retain a tooth with an irreversibly damaged nerve...</p>
  </div>
</section>

<section>
  <h2 class="abs section-title" style="left:152px;top:1410px">Videos</h2>
  <div class="abs rule" style="left:130px;top:1450px;width:455px"></div>
  <div class="abs video" role="img" aria-label="Video still of a child at a dental check-up"></div>
  <div class="abs play"><svg width="42" height="42" viewBox="0 0 42 42"><path d="M17 14l11 7-11 7z" fill="#1ba3e0"/></svg></div>
  <p class="abs video-caption">Lorem Ipsum is simply dummy text</p>

  <h2 class="abs section-title" style="left:620px;top:1410px">What Our <em>Customers are Saying!</em></h2>
  <div class="abs rule" style="left:608px;top:1450px;width:460px"></div>
  <div class="abs quote-mark" style="left:633px;top:1475px">“</div>
  <p class="abs quote-text">Lorem Ipsum is simply dummy text of the printing and typesetting industry. Lorem Ipsum has been the industry's standard dummy text ever since the 1500s, when an unknown printer took a galley of type and scrambled it to make a type specimenbook. It has survived not only five centuries,</p>
  <div class="abs quote-mark" style="left:962px;top:1635px">”</div>
  <div class="abs avatar" role="img" aria-label="Portrait of the customer"></div>
  <p class="abs author">Glenn Forster<small>Publisher</small></p>
  <div class="abs circle-arrow" style="left:948px;top:1718px"><svg width="10" height="10"><path d="M7 1 3 5l4 4" fill="none" stroke="#777" stroke-width="1.5"/></svg></div>
  <div class="abs circle-arrow on" style="left:980px;top:1718px"><svg width="10" height="10"><path d="M3 1l4 4-4 4" fill="none" stroke="#1ba3e0" stroke-width="1.5"/></svg></div>
</section>

<section>
  <h2 class="abs section-title" style="left:155px;top:1815px">Team <em>Members</em></h2>
  <span class="abs view-team">View Team</span>
  <div class="abs rule" style="left:130px;top:1857px;width:938px"></div>

  <div class="abs card" style="left:155px"><div class="card-photo" role="img" aria-label="Portrait of Mark Rowan"></div><div class="card-bar"><b>Mark Rowan</b><span>Founder of dentist</span><div class="card-tag"><i></i><i></i><i></i></div></div></div>
  <div class="abs card" style="left:383px"><div class="card-photo" role="img" aria-label="Portrait of Jamie Doyle"></div><div class="card-bar"><b>Jamie Doyle</b><span>Implant Expert</span><div class="card-tag"><i></i><i></i><i></i></div></div></div>
  <div class="abs card" style="left:612px"><div class="card-photo" role="img" aria-label="Portrait of Dr. Sarah Linden"></div><div class="card-bar"><b>Dr. Sarah Linden</b><span>Founder of dentist</span><div class="card-tag"><i></i><i></i><i></i></div></div></div>
  <div class="abs card" style="left:840px"><div class="card-photo" role="img" aria-label="Portrait of Dr. Jake Dorran"></div><div class="card-bar"><b>Dr. Jake Dorran</b><span>Implant Expert</span><div class="card-tag"><i></i><i></i><i></i></div></div></div>
</section>

<footer>
  <div class="abs footer"></div>
  <h3 class="abs foot-title" style="left:155px;top:2196px">News Letter</h3>
  <div class="abs foot-rule" style="left:155px;top:2226px;width:305px"></div>
  <p class="abs foot-text" style="left:155px;top:2240px;width:210px">Receive up to date information about current and upcoming events.</p>
  <div class="abs field" style="top:2278px">Name</div>
  <div class="abs field" style="top:2313px">Email</div>
  <div class="abs submit">SUBMIT</div>

  <h3 class="abs foot-title" style="left:535px;top:2196px">Quick LInk</h3>
  <div class="abs foot-rule" style="left:535px;top:2226px;width:155px"></div>
  <ul class="abs quick">
    <li class="active">Home</li><li>About</li><li>Team</li><li>Dental Treatments</li><li>Dental Advice</li><li>Contact</li>
  </ul>

  <h3 class="abs foot-title" style="left:765px;top:2196px">Contact Info</h3>
  <div class="abs foot-rule" style="left:765px;top:2226px;width:280px"></div>
  <p class="abs foot-text" style="left:765px;top:2240px;width:230px">Unit 7, 18 Seabreeze Parade,<br>Kelmore, WA 6071</p>
  <p class="abs foot-text" style="left:765px;top:2283px">Phone:<br>08 5550 1847</p>
  <p class="abs foot-text" style="left:765px;top:2325px">Email:<br>info@harbourlight-dental.com</p>

  <p class="abs copyright">© 2016 The Harbourlight.  All rights reserved.</p>
  <span class="abs social" style="left:958px"></span>
  <span class="abs social" style="left:988px;background:var(--blue)"></span>
  <span class="abs social" style="left:1020px"></span>
</footer>

</body>
</html>
```